PDN Letterhead

We need a letterhead design that will be able to be used on all marketing products (letterhead, mail chimp, envelops, business cards, etc.) We are a law firm specializing primarily in transportation law but offer a wide range of services to our clients. We would like the design to be modern, simple, and professional. Our colors are black and gold, however, we've incorporated dark gray and white on other marketing products such as our website.

```html
<!DOCTYPE html>
<html lang="en">
<head>
<meta charset="utf-8">
<title>PDN Law Group – Business Cards</title>
<link href="https://fonts.googleapis.com/css2?family=Cinzel:wght@400;500&display=swap" rel="stylesheet">
<style>
  :root {
    --gold: #bda47f;
    --black: #0d0d0d;
    --white: #ffffff;
    --paper: #efefef;
    --ink: #1a1a1a;
  }
  * { margin: 0; padding: 0; box-sizing: border-box; }
  html, body {
    width: 1200px; height: 910px; overflow: hidden;
    background: var(--paper);
    font-family: "Cinzel", "Times New Roman", serif;
    color: var(--ink);
  }
  .canvas { position: relative; width: 1200px; height: 910px; }
  .card {
    position: absolute; top: 300px;
    width: 540px; height: 309px;
    background: var(--white);
    box-shadow: 0 2px 3px rgba(0,0,0,.08), 0 12px 30px rgba(0,0,0,.10);
    overflow: hidden;
  }
  .card--front { left: 40px; }
  .card--back { left: 620px; }
  .card__shapes { position: absolute; inset: 0; }
  .band { fill: var(--gold); }
  .corner { fill: var(--black); }

  .wordmark { position: absolute; color: var(--black); font-weight: 400; line-height: 1; }
  .wordmark__name { display: block; letter-spacing: .08em; }
  .wordmark__sub { display: block; letter-spacing: .32em; }
  .card--front .wordmark { left: 110px; top: 112px; }
  .card--front .wordmark__name { font-size: 62px; }
  .card--front .wordmark__sub { font-size: 20px; margin-top: 10px; }
  .card--back .wordmark { left: 42px; top: 118px; }
  .card--back .wordmark__name { font-size: 40px; }
  .card--back .wordmark__sub { font-size: 13px; margin-top: 7px; }

  .name-tag {
    position: absolute; left: 158px; top: 38px;
    background: var(--black); color: var(--white);
    padding: 8px 14px 7px; text-align: center; line-height: 1.05;
  }
  .name-tag__name { display: block; font-size: 17px; letter-spacing: .04em; }
  .name-tag__role { display: block; font-size: 11px; letter-spacing: .08em; }

  .contact { position: absolute; left: 42px; top: 196px; list-style: none; }
  .contact__item {
    display: flex; align-items: flex-start; gap: 9px;
    font-size: 12.5px; line-height: 1.15; margin-bottom: 5px; letter-spacing: .02em;
  }
  .contact__icon { width: 11px; height: 11px; flex: none; margin-top: 1px; fill: var(--gold); }
</style>
</head>
<body>
<main class="canvas">

  <section class="card card--front" aria-label="Business card front">
    <svg class="card__shapes" viewBox="0 0 540 309" aria-hidden="true">
      <polygon class="band" points="400,0 432,0 540,122 540,158"/>
      <polygon class="corner" points="462,0 540,0 540,88"/>
    </svg>
    <div class="wordmark">
      <span class="wordmark__name">PDN</span>
      <span class="wordmark__sub">Law Group</span>
    </div>
  </section>

  <section class="card card--back" aria-label="Business card back">
    <svg class="card__shapes" viewBox="0 0 540 309" aria-hidden="true">
      <polygon class="band" points="285,0 335,0 540,235 540,292"/>
      <polygon class="corner" points="390,0 540,0 540,172"/>
    </svg>
    <div class="name-tag">
      <span class="name-tag__name">Avery Lane</span>
      <span class="name-tag__role">Director</span>
    </div>
    <div class="wordmark">
      <span class="wordmark__name">PDN</span>
      <span class="wordmark__sub">Law Group</span>
    </div>
    <ul class="contact">
      <li class="contact__item">
        <svg class="contact__icon" viewBox="0 0 12 12" aria-hidden="true"><path d="M2.5 1 L4.5 1 L5.3 3.6 L4 4.6 Q5 7 7.4 8 L8.4 6.7 L11 7.5 L11 9.5 Q11 11 9.5 11 Q1 10.5 1 2.5 Q1 1 2.5 1Z"/></svg>
        <span>555.010.2840</span>
      </li>
      <li class="contact__item">
        <svg class="contact__icon" viewBox="0 0 12 12" aria-hidden="true"><path d="M1 2.5 H11 V3.3 L6 6.6 L1 3.3Z M1 4.5 L6 7.8 L11 4.5 V10 H1Z"/></svg>
        <span>ADMIN@PDNLEGAL.COM</span>
      </li>
      <li class="contact__item">
        <svg class="contact__icon" viewBox="0 0 12 12" aria-hidden="true"><circle cx="6" cy="6" r="5"/></svg>
        <span>WWW.PDNLEGAL.COM</span>
      </li>
      <li class="contact__item">
        <svg class="contact__icon" viewBox="0 0 12 12" aria-hidden="true"><path d="M6 0.5 A4 4 0 0 1 10 4.5 Q10 7 6 11.5 Q2 7 2 4.5 A4 4 0 0 1 6 0.5Z M6 3 A1.5 1.5 0 1 0 6 6 A1.5 1.5 0 1 0 6 3Z" fill-rule="evenodd"/></svg>
        <span>240 HARBOR VIEW<br>AVENUE, SUITE 310</span>
      </li>
    </ul>
  </section>

</main>
</body>
</html>
```